Corvella Group Tank Card. New Design

We need a new design for our Credit Card Tank. We want a modern design using our logo colors. Our Card measures are 8,5cmX5,5cm. You can upgrade our logo design too. We are looking for modern and cool design. Our card printers can print the card number and holder in white color then you can use the colors you want for the background.

Target Market(s)

Gas station customers

Industry/Entity Type

Credit Card

Font styles to use
Sans Serif

Colors
a54499
b768aa
d2a4cc
acd036
cadf82
9bcb3b

Requirements
Must have
• Cool Design

```html
<!DOCTYPE html>
<html lang="en">
<head>
<meta charset="utf-8">
<title>Corvella Group Tank Card</title>
<link href="https://fonts.googleapis.com/css2?family=Montserrat:wght@500;600;700&family=Share+Tech+Mono&display=swap" rel="stylesheet">
<style>
  :root {
    --page-bg: #f2f2f2;
    --card-magenta: #c0369a;
    --card-deep: #7e1f78;
    --card-bright: #d24fb6;
    --card-soft: #b768aa;
    --stripe: #050505;
    --white: #ffffff;
    --chip-light: #f4c872;
    --chip-dark: #c8892c;
    --chip-line: #a06a1e;
    --card-shadow: rgba(40, 20, 40, 0.28);
  }
  * { box-sizing: border-box; margin: 0; padding: 0; }
  html, body {
    width: 1076px;
    height: 1200px;
    overflow: hidden;
    background: var(--page-bg);
  }
  .canvas {
    position: relative;
    width: 1076px;
    height: 1200px;
    font-family: "Montserrat", Arial, sans-serif;
    color: var(--white);
  }
  .card {
    position: absolute;
    left: 158px;
    width: 760px;
    height: 492px;
    border-radius: 40px;
    overflow: hidden;
    box-shadow: 0 24px 40px var(--card-shadow);
  }
  .card--front { top: 80px; }
  .card--back  { top: 628px; background: var(--card-magenta); }

  .card__visual {
    position: absolute;
    inset: 0;
    background:
      radial-gradient(ellipse 70% 55% at 75% 25%, rgba(230, 120, 210, 0.55), transparent 70%),
      radial-gradient(ellipse 60% 40% at 30% 85%, rgba(90, 20, 90, 0.45), transparent 70%),
      linear-gradient(160deg, var(--card-deep) 0%, var(--card-magenta) 45%, var(--card-bright) 75%, var(--card-magenta) 100%);
  }

  .brand {
    position: absolute;
    display: flex;
    align-items: center;
    gap: 14px;
    font-weight: 600;
    letter-spacing: 1px;
    text-transform: uppercase;
    color: var(--white);
  }
  .brand__dot {
    border: 4px solid var(--white);
    border-radius: 50%;
  }
  .card--front .brand { left: 70px; top: 88px; font-size: 30px; }
  .card--front .brand__dot { width: 50px; height: 50px; }
  .card--back .brand { left: 56px; top: 248px; font-size: 22px; }
  .card--back .brand__dot { width: 36px; height: 36px; border-width: 3px; }

  .chip {
    position: absolute;
    left: 589px;
    top: 218px;
    width: 107px;
    height: 86px;
  }

  .card__holder,
  .card__number,
  .card__valid {
    position: absolute;
    font-family: "Share Tech Mono", "Courier New", monospace;
    color: var(--white);
  }
  .card__holder {
    left: 64px;
    top: 250px;
    font-size: 30px;
    letter-spacing: 3px;
  }
  .card__number {
    left: 64px;
    top: 330px;
    width: 632px;
    display: flex;
    justify-content: space-between;
    font-size: 42px;
    letter-spacing: 4px;
  }
  .card__valid {
    right: 64px;
    top: 402px;
    display: flex;
    align-items: center;
    gap: 10px;
    font-size: 30px;
    letter-spacing: 2px;
  }
  .card__valid-label {
    font-size: 11px;
    letter-spacing: 1px;
  }

  .stripe {
    position: absolute;
    left: 0;
    top: 75px;
    width: 100%;
    height: 92px;
    background: var(--stripe);
  }
  .address {
    position: absolute;
    left: 56px;
    top: 352px;
    font-style: normal;
    font-size: 20px;
    font-weight: 500;
    line-height: 1.4;
  }
  .website {
    position: absolute;
    right: 52px;
    top: 436px;
    font-size: 18px;
    font-weight: 700;
  }
</style>
</head>
<body>
<main class="canvas">

  <section class="card card--front" aria-label="Card front">
    <div class="card__visual" role="img" aria-label="Magenta-toned photograph of a curved modern roof over a city skyline"></div>

    <div class="brand"><span class="brand__dot"></span>Corvella Group</div>

    <svg class="chip" viewBox="0 0 107 86" aria-hidden="true">
      <defs>
        <linearGradient id="chipGold" x1="0" y1="0" x2="1" y2="1">
          <stop offset="0" stop-color="var(--chip-light)"/>
          <stop offset="1" stop-color="var(--chip-dark)"/>
        </linearGradient>
      </defs>
      <rect x="1" y="1" width="105" height="84" rx="16" fill="url(#chipGold)"/>
      <g fill="none" stroke="var(--chip-line)" stroke-width="2">
        <path d="M1 28 H34 M1 58 H34 M73 28 H106 M73 58 H106"/>
        <path d="M34 1 V28 Q34 43 42 43 Q34 43 34 58 V85"/>
        <path d="M73 1 V28 Q73 43 65 43 Q73 43 73 58 V85"/>
        <rect x="42" y="22" width="23" height="42" rx="10"/>
      </g>
    </svg>

    <p class="card__holder">NAME NAME NAME</p>
    <p class="card__number"><span>1234</span><span>5478</span><span>9012</span><span>3456</span></p>
    <p class="card__valid"><span class="card__valid-label">VALID ▸</span>20/04/17</p>
  </section>

  <section class="card card--back" aria-label="Card back">
    <div class="stripe"></div>
    <div class="brand"><span class="brand__dot"></span>Corvella Group</div>
    <address class="address">
      Carrer del Molí, 24,<br>
      17482 Valdoria,<br>
      Girona, Espanha
    </address>
    <p class="website">www.corvellagroup.eu</p>
  </section>

</main>
</body>
</html>
```